The Hollowmere Stillhouse - Gin Bottle Label

Hi Designers,

We are currently looking for some fresh ideas regarding a label for our gin bottle. We are relatively small and with an emphasis on a quality tipple
made from the very finest and responsibly sourced botanicals. Our operation concentrates on small batch/hand crafted in its purest sense and we would like to reflect this in our brand.
We are looking for a label to read The Hollowmere Stillhouse and have feminine accents with a primary background colour similar to Wrenfield green/blue. Things like Sakura branches with blossom, floral, pretty scrolling perhaps around either full or partial boarder. Gold foil might be used to accent the black border/highlight the word "Hollowmere" and perhaps any floral pattern.
There could reconsideration given to include two boxes "Batch No" and "Bottle No" which would remain empty and filled out by hand during bottling.
Our gin will be 45%ABV
Some floral designs might look good as though they were watercolours in appearance perhaps.
Our bottles are clear medicine style of which I shall attatch a pic.
We are pretty excited about this and would invite anyone with flair and great ideas to have fun with this design.

With kind regards,

Max

Target Market(s)

People who adore bespoke Gin and would be predominately female.

Colors
86cfc6

Requirements
Must have
• We love the Wrenfield green tones and this well may be our label colour with your design.
• The Hollowmere Stillhouse - Gin - 45ABV
Nice to have
• Batch No & Bottle No boxes

```html
<!DOCTYPE html>
<html lang="en">
<head>
<meta charset="utf-8">
<title>The Hollowmere Stillhouse – Gin Label</title>
<link rel="stylesheet" href="https://fonts.googleapis.com/css2?family=Great+Vibes&family=Open+Sans:wght@400&family=Arimo:wght@700&display=swap">
<style>
  :root {
    --page: #ffffff;
    --mint: #9ef3cf;
    --mint-deep: #8de6c4;
    --ink-blue: #1b1a8f;
    --gold: #c9a94e;
    --ink: #111111;
    --field: #ffffff;
  }
  * { margin: 0; padding: 0; box-sizing: border-box; }
  html, body {
    width: 1200px;
    height: 1200px;
    overflow: hidden;
    background: var(--page);
  }
  .canvas {
    position: relative;
    width: 1200px;
    height: 1200px;
  }
  .label {
    position: absolute;
    left: 5px;
    top: 326px;
    width: 1191px;
    height: 546px;
    overflow: hidden;
  }
  .label__pattern {
    position: absolute;
    inset: 0;
    width: 100%;
    height: 100%;
  }
  .label__name {
    position: absolute;
    left: 0;
    width: 100%;
    font-family: "Great Vibes", cursive;
    font-weight: 400;
    font-size: 128px;
    color: var(--ink-blue);
    -webkit-text-stroke: 3px var(--ink-blue);
    text-shadow:
      1px 1px 0 var(--gold),
      -1px -1px 0 var(--gold),
      1px -1px 0 var(--gold),
      -1px 1px 0 var(--gold),
      2px 3px 3px rgba(20, 40, 60, 0.35);
    text-align: center;
    line-height: 1;
    white-space: nowrap;
  }
  .label__name--top {
    top: 58px;
    padding-right: 56px;
  }
  .label__name--bottom {
    top: 218px;
    padding-right: 8px;
  }
  .label__strength {
    position: absolute;
    left: 447px;
    top: 382px;
    font-family: "Open Sans", sans-serif;
    font-size: 60px;
    font-weight: 400;
    color: var(--ink);
    letter-spacing: -1px;
    line-height: 1;
  }
  .fill-box {
    position: absolute;
    top: 484px;
    width: 342px;
    height: 44px;
    background: var(--field);
    padding-left: 16px;
    display: flex;
    align-items: center;
    font-family: "Arimo", sans-serif;
    font-weight: 700;
    font-size: 30px;
    color: var(--ink);
  }
  .fill-box--batch { left: 31px; }
  .fill-box--bottle { left: 821px; }
</style>
</head>
<body>
<div class="canvas">
  <section class="label">
    <svg class="label__pattern" role="img" aria-label="Watercolour botanical pattern of leaves, berry sprigs and pale yellow blossoms on mint green" viewBox="0 0 1191 546" preserveAspectRatio="none">
      <defs>
        <linearGradient id="mintWash" x1="0" y1="0" x2="1" y2="1">
          <stop offset="0" stop-color="#a4f5d3"/>
          <stop offset="1" stop-color="#93eac7"/>
        </linearGradient>
        <radialGradient id="blushYellow">
          <stop offset="0" stop-color="#e6f5a8" stop-opacity="0.55"/>
          <stop offset="1" stop-color="#e6f5a8" stop-opacity="0"/>
        </radialGradient>
        <radialGradient id="blushWhite">
          <stop offset="0" stop-color="#e8fff4" stop-opacity="0.5"/>
          <stop offset="1" stop-color="#e8fff4" stop-opacity="0"/>
        </radialGradient>
        <radialGradient id="blushTeal">
          <stop offset="0" stop-color="#6fc7a9" stop-opacity="0.35"/>
          <stop offset="1" stop-color="#6fc7a9" stop-opacity="0"/>
        </radialGradient>
      </defs>
      <rect width="1191" height="546" fill="url(#mintWash)"/>
      <ellipse cx="1000" cy="80" rx="220" ry="120" fill="url(#blushYellow)"/>
      <ellipse cx="320" cy="480" rx="240" ry="110" fill="url(#blushYellow)"/>
      <ellipse cx="1050" cy="380" rx="200" ry="130" fill="url(#blushYellow)"/>
      <ellipse cx="130" cy="110" rx="200" ry="120" fill="url(#blushWhite)"/>
      <ellipse cx="1110" cy="230" rx="160" ry="110" fill="url(#blushWhite)"/>
      <ellipse cx="700" cy="500" rx="260" ry="90" fill="url(#blushWhite)"/>
      <ellipse cx="110" cy="330" rx="160" ry="140" fill="url(#blushTeal)"/>
      <ellipse cx="1080" cy="470" rx="170" ry="90" fill="url(#blushTeal)"/>
      <ellipse cx="600" cy="40" rx="260" ry="70" fill="url(#blushTeal)"/>
    </svg>
    <h1 class="label__name label__name--top">The Hollowmere</h1>
    <p class="label__name label__name--bottom">Stillhouse</p>
    <p class="label__strength">45%ABV</p>
    <div class="fill-box fill-box--batch">Batch No :</div>
    <div class="fill-box fill-box--bottle">Bottle No :</div>
  </section>
</div>
</body>
</html>
```